business card design and letterhead for a building inspection company. We have a pre-purchase building and pest inspection ( i inspect house before people purchase it)
Updates

Linda has been so so responsive and good, i highly recommend her

Industry/Entity Type

Building

Contact Information for Business Card

audience, solicitor, real estate agent, mortgage brokerthe rest of the info will be in the attachement business card

```html
<!DOCTYPE html>
<html lang="en">
<head>
<meta charset="utf-8">
<title>Truehold Property Inspections – Stationery</title>
<link rel="stylesheet" href="https://fonts.googleapis.com/css2?family=Lato:wght@400;700;900&display=swap">
<style>
  :root{
    --blue:#1f7ac8;
    --ink:#1b1b1b;
    --paper:#ffffff;
    --ground:#d9d7d8;
    --faint:#e6e6e6;
    --muted:#555555;
  }
  *{box-sizing:border-box;margin:0;padding:0}
  html,body{width:1200px;height:843px;overflow:hidden}
  body{background:var(--ground);font-family:"Lato",sans-serif;color:var(--ink);position:relative}

  .brand{display:flex;align-items:center;gap:8px}
  .brand-mark{width:14px;height:14px;border-radius:50%;background:currentColor;flex:none}
  .brand-name{font-weight:900;text-transform:uppercase;letter-spacing:.04em;line-height:1}
  .brand-sub{font-weight:400;font-size:7px;letter-spacing:.12em;text-transform:uppercase;margin-top:3px;line-height:1.3}
  .brand-sub .tagline{display:block;text-transform:none;letter-spacing:.22em}

  /* Letterhead */
  .letterhead{position:absolute;left:650px;top:80px;width:480px;height:679px;background:var(--paper);box-shadow:0 4px 14px rgba(0,0,0,.18);overflow:hidden}
  .letterhead .brand{position:absolute;left:40px;top:44px;color:var(--blue)}
  .letterhead .brand-name{font-size:24px}
  .letterhead .brand-sub{color:var(--ink)}
  .letterhead .brand-sub .tagline{color:var(--blue)}
  .letterhead .contact{position:absolute;right:40px;top:44px}
  .sender-name{color:var(--blue);font-weight:900;font-size:9px;letter-spacing:.05em;text-transform:uppercase;margin-bottom:5px}
  .contact-list{list-style:none;font-size:7px;color:var(--muted);line-height:1.55}
  .contact-list li{display:flex;align-items:center;gap:5px}
  .contact-list svg{width:7px;height:7px;flex:none;fill:var(--blue)}
  .watermark{position:absolute;right:50px;bottom:120px;width:190px;height:190px;border-radius:50%;background:var(--faint)}
  .lh-footer{position:absolute;left:0;right:0;bottom:0;height:48px}
  .lh-footer .tab{position:absolute;left:0;bottom:0;width:62%;height:40px;background:var(--blue);border-top-right-radius:10px;display:flex;align-items:center;padding-left:40px;color:#fff;font-size:11px;letter-spacing:.06em}
  .lh-footer .strip{position:absolute;right:0;bottom:0;width:40%;height:20px;background:var(--blue)}
  .lh-footer .rule{position:absolute;right:0;bottom:20px;width:40%;height:6px;background:var(--ink)}

  /* Business cards */
  .card{position:absolute;width:360px;height:206px;box-shadow:0 4px 12px rgba(0,0,0,.2);overflow:hidden}
  .card-back{left:60px;top:160px;background:var(--blue);color:#fff}
  .card-back .brand{position:absolute;left:40px;top:64px;color:#fff}
  .card-back .brand-name{font-size:24px}
  .card-back .services{position:absolute;left:40px;bottom:42px;font-size:9px;font-weight:700;letter-spacing:.06em}
  .card-front{left:60px;top:460px;background:var(--paper)}
  .card-front .brand{position:absolute;left:26px;top:26px;color:var(--blue)}
  .card-front .brand-name{font-size:18px}
  .card-front .brand-sub{color:var(--ink);font-size:6px}
  .card-front .brand-sub .tagline{color:var(--blue)}
  .card-front .sender-name{position:absolute;left:26px;top:84px;font-size:11px}
  .card-front .contact-list{position:absolute;left:26px;top:106px;font-size:7.5px}
  .card-front .watermark{right:18px;top:20px;bottom:auto;width:110px;height:110px}
  .card-front .rule{position:absolute;right:0;bottom:22px;width:58%;height:5px;background:var(--ink)}
  .card-front .strip{position:absolute;right:0;bottom:0;width:58%;height:22px;background:var(--blue);border-top-left-radius:8px}
</style>
</head>
<body>

<svg width="0" height="0" style="position:absolute" aria-hidden="true">
  <symbol id="icon-phone" viewBox="0 0 10 10"><path d="M2 0.5 L3.8 2.6 L2.8 3.6 C3.5 5 5 6.5 6.4 7.2 L7.4 6.2 L9.5 8 L8.2 9.5 C4.5 9 1 5.5 0.5 1.8 Z"/></symbol>
  <symbol id="icon-mobile" viewBox="0 0 10 10"><path d="M2.5 0 H7.5 V10 H2.5 Z M3.3 1 V8 H6.7 V1 Z"/></symbol>
  <symbol id="icon-mail" viewBox="0 0 10 10"><path d="M0 2 H10 V8 H0 Z M0.8 2.6 L5 5.6 L9.2 2.6 V3.4 L5 6.4 L0.8 3.4 Z" fill-rule="evenodd"/></symbol>
  <symbol id="icon-web" viewBox="0 0 10 10"><path d="M5 0 A5 5 0 1 1 4.99 0 Z M5 1.2 A3.8 3.8 0 1 0 5.01 1.2 Z" fill-rule="evenodd"/><rect x="0.5" y="4.5" width="9" height="1"/></symbol>
</svg>

<article class="letterhead" aria-label="Letterhead">
  <div class="brand">
    <span class="brand-mark"></span>
    <div>
      <div class="brand-name">Truehold</div>
      <div class="brand-sub">Property Inspections<span class="tagline">The building and pest expert</span></div>
    </div>
  </div>
  <div class="contact">
    <p class="sender-name">Marco Delane</p>
    <ul class="contact-list">
      <li><svg><use href="#icon-phone"/></svg>(02) 9000 1234</li>
      <li><svg><use href="#icon-mobile"/></svg>0400 111 222</li>
      <li><svg><use href="#icon-mail"/></svg>info@trueholdinspect.com.au</li>
      <li><svg><use href="#icon-web"/></svg>www.trueholdinspect.com.au</li>
    </ul>
  </div>
  <div class="watermark" aria-hidden="true"></div>
  <footer class="lh-footer">
    <div class="rule"></div>
    <div class="strip"></div>
    <div class="tab">Property Inspection | Property Maintenance</div>
  </footer>
</article>

<article class="card card-back" aria-label="Business card back">
  <div class="brand">
    <span class="brand-mark"></span>
    <div>
      <div class="brand-name">Truehold</div>
      <div class="brand-sub">Property Inspections<span class="tagline">The building and pest expert</span></div>
    </div>
  </div>
  <p class="services">Property Inspection | Property Maintenance</p>
</article>

<article class="card card-front" aria-label="Business card front">
  <div class="watermark" aria-hidden="true"></div>
  <div class="brand">
    <span class="brand-mark"></span>
    <div>
      <div class="brand-name">Truehold</div>
      <div class="brand-sub">Property Inspections<span class="tagline">The building and pest expert</span></div>
    </div>
  </div>
  <p class="sender-name">Marco Delane</p>
  <ul class="contact-list">
    <li><svg><use href="#icon-phone"/></svg>(02) 9000 1234</li>
    <li><svg><use href="#icon-mobile"/></svg>0400 111 222</li>
    <li><svg><use href="#icon-mail"/></svg>info@trueholdinspect.com.au</li>
    <li><svg><use href="#icon-web"/></svg>www.trueholdinspect.com.au</li>
  </ul>
  <div class="rule"></div>
  <div class="strip"></div>
</article>

</body>
</html>
```